Dr. Marissa Tevlin Medical/Chiropractic Business Card

Dr. Tevlin is a chiropractor and will require a business card that she uses every single day to book appointments on the back side of the card. Currently the office name goes by Dr. Marissa Tevlin. The chiropractic profession is based on the diagnosis and manipulative treatment of misalignments of the joints, especially those of the spinal column, which are held to cause other disorders by affecting the nerves, muscles, and organs. Dr. Marissa Tevlin is looking for a contemporary and minimalistic design.

Industry/Entity Type

Medical

Contact Information for Business Card

Name: Dr. Marissa Tevlin; Address: 748 Harcastle Rd South, London, ON N5R 2K7; Phone Number: 519.274.6193; Fax: 519.281.5046; email: marissa.tevlin@quorvamail.com

Requirements
Must have
• ability to write multiple appointments date/time on the back of card

```html
<!DOCTYPE html>
<html lang="en">
<head>
<meta charset="utf-8">
<title>Dr. Marissa Tevlin – Business Card</title>
<link href="https://fonts.googleapis.com/css2?family=Ubuntu:wght@500;700&family=Mulish:ital,wght@0,400;0,600;1,400&display=swap" rel="stylesheet">
<style>
  :root {
    --navy: #231c53;
    --paper: #ffffff;
    --backdrop: #b9babd;
    --muted: #b8b6cc;
    --label: #5a5670;
    --rule: #7a7690;
  }
  * { margin: 0; padding: 0; box-sizing: border-box; }
  html, body { width: 1200px; height: 1200px; overflow: hidden; }
  body {
    background: var(--backdrop);
    display: flex;
    flex-direction: column;
    align-items: center;
    justify-content: center;
    gap: 60px;
    font-family: "Mulish", sans-serif;
  }
  .card {
    position: relative;
    width: 900px;
    height: 514px;
    background: var(--navy);
    overflow: hidden;
    box-shadow: 0 6px 18px rgba(0,0,0,0.18);
  }
  .card-art { position: absolute; inset: 0; width: 100%; height: 100%; }

  /* Back: appointments */
  .appt-title {
    position: absolute; left: 44px; top: 20px;
    font-family: "Ubuntu", sans-serif; font-weight: 700;
    font-size: 30px; color: var(--paper); letter-spacing: 1px;
  }
  .appt-list {
    position: absolute; left: 450px; top: 150px; width: 410px;
    list-style: none; display: flex; flex-direction: column; gap: 40px;
  }
  .appt-row {
    display: flex; align-items: baseline; gap: 8px;
    font-size: 19px; font-style: italic; color: var(--label);
  }
  .appt-fill { flex: 1; border-bottom: 2px dotted var(--rule); height: 1px; }
  .appt-fill.date { flex: 1.2; }
  .appt-note {
    position: absolute; left: 44px; bottom: 36px;
    font-size: 17px; font-style: italic; line-height: 1.4; color: var(--muted);
  }

  /* Front: identity */
  .identity {
    position: absolute; right: 44px; top: 70px; text-align: right; color: var(--paper);
  }
  .identity-name { font-family: "Ubuntu", sans-serif; font-weight: 700; font-size: 44px; }
  .identity-role { font-size: 26px; margin-top: 2px; }
  .contact {
    position: absolute; left: 50px; top: 62px; list-style: none;
    color: var(--navy); font-size: 26px; line-height: 1.15;
    display: flex; flex-direction: column; gap: 12px;
  }
  .contact-icon { display: block; width: 16px; height: 16px; margin-bottom: 2px; }
</style>
</head>
<body>

<section class="card card-back" aria-label="Appointment side">
  <svg class="card-art" viewBox="0 0 900 514" aria-hidden="true">
    <path class="panel-light" fill="var(--paper)" d="M320 0 H900 V514 H620 C540 330 260 260 260 130 C260 60 290 20 320 0 Z"/>
  </svg>
  <h2 class="appt-title">Appointments</h2>
  <ul class="appt-list">
    <li class="appt-row">Date <span class="appt-fill date"></span> Time <span class="appt-fill"></span></li>
    <li class="appt-row">Date <span class="appt-fill date"></span> Time <span class="appt-fill"></span></li>
    <li class="appt-row">Date <span class="appt-fill date"></span> Time <span class="appt-fill"></span></li>
  </ul>
  <p class="appt-note">If you are unable to make your appointment,<br>Please call us to reschedule.</p>
</section>

<section class="card card-front" aria-label="Contact side">
  <svg class="card-art" viewBox="0 0 900 514" aria-hidden="true">
    <path class="panel-light" fill="var(--paper)" d="M0 0 H320 C420 200 880 300 880 420 C880 460 840 462 0 470 Z"/>
  </svg>

  <ul class="contact">
    <li>
      <svg class="contact-icon" viewBox="0 0 16 16" aria-label="Phone"><circle cx="8" cy="8" r="8" fill="var(--navy)"/><path d="M5 4.5 L6.5 4.5 L7.2 6.3 L6.3 7 C6.8 8 7.8 9 8.9 9.6 L9.6 8.7 L11.4 9.4 L11.4 10.9 C8 11 5 8 5 4.5 Z" fill="#fff"/></svg>
      519.274.6193
    </li>
    <li>
      <svg class="contact-icon" viewBox="0 0 16 16" aria-label="Fax"><circle cx="8" cy="8" r="8" fill="var(--navy)"/><rect x="4.5" y="6" width="7" height="5" rx="1" fill="#fff"/><rect x="6" y="4" width="4" height="2.5" fill="#fff"/></svg>
      519.281.5046
    </li>
    <li>
      <svg class="contact-icon" viewBox="0 0 16 16" aria-label="Email"><circle cx="8" cy="8" r="8" fill="var(--navy)"/><rect x="4.2" y="5.2" width="7.6" height="5.6" rx="0.8" fill="#fff"/><path d="M4.6 5.6 L8 8.3 L11.4 5.6" fill="none" stroke="var(--navy)" stroke-width="0.9"/></svg>
      marissa.tevlin@quorvamail.com
    </li>
    <li>
      <svg class="contact-icon" viewBox="0 0 16 16" aria-label="Address"><circle cx="8" cy="8" r="8" fill="var(--navy)"/><path d="M8 3.5 C6.2 3.5 5 4.8 5 6.4 C5 8.6 8 12.2 8 12.2 C8 12.2 11 8.6 11 6.4 C11 4.8 9.8 3.5 8 3.5 Z" fill="#fff"/><circle cx="8" cy="6.4" r="1.1" fill="var(--navy)"/></svg>
      748 Harcastle Rd South<br>London, ON N5R 2K7
    </li>
  </ul>

  <div class="identity">
    <h1 class="identity-name">Dr. Marissa Tevlin</h1>
    <p class="identity-role">Chiropractor</p>
  </div>
</section>

</body>
</html>
```